Birchmead Assurance Group Ltd needs a business card and logo

We need a logo for documents, invoices etc and a business card to match. We are a health auditing, training and consulting company based in NZ and working in both Australia and NZ. We ensure health organisations meet all their compliance requirements and develop expertise in the health auditing sector. The design should in some way reflect either symbols for quality management in the health sector.

Target Market(s)

Health providers and those wishing to increase their capability in meeting and understanding compliance requirements

Industry/Entity Type

Business

Contact Information for Business Card

Logo plus contact details

Logo Text

Health auditing, consultancy and training

Requirements
Must have
• Name and contact details director: Clara Hotham, chotham@bag-example.co.nz, PO Box 419, Kowhai Ridge, KR, cell +6427390516

```html
<!DOCTYPE html>
<html lang="en">
<head>
<meta charset="utf-8">
<title>Birchmead Assurance Group Ltd — Business Card</title>
<link href="https://fonts.googleapis.com/css2?family=Montserrat:wght@300&family=Open+Sans:wght@400&display=swap" rel="stylesheet">
<style>
  :root {
    --backdrop: #bf9a72;
    --card: #0c0c0c;
    --gold: #cfae55;
    --red: #c8322b;
    --text-light: #d9d6d0;
    --rule: #a3302a;
  }
  * { margin: 0; padding: 0; box-sizing: border-box; }
  html, body { width: 1200px; height: 1200px; overflow: hidden; }
  body {
    background: var(--backdrop);
    position: relative;
    font-family: "Open Sans", sans-serif;
  }
  .card {
    position: absolute;
    left: 287px;
    width: 626px;
    height: 389px;
    background: var(--card);
  }
  .card--front { top: 150px; }
  .card--back { top: 681px; }

  .wordmark {
    position: absolute;
    display: flex;
    align-items: center;
    color: var(--gold);
    font-family: "Open Sans", sans-serif;
    font-weight: 400;
  }
  .wordmark__dot {
    flex: none;
    border-radius: 50%;
    background: var(--red);
  }
  .wordmark__name { line-height: 1.1; }
  .wordmark__main { display: block; letter-spacing: 0.08em; }
  .wordmark__sub { display: block; }

  .card--front .wordmark { left: 50px; top: 160px; }
  .card--front .wordmark__dot { width: 26px; height: 26px; margin-right: 12px; }
  .card--front .wordmark__main { font-size: 30px; }
  .card--front .wordmark__sub { font-size: 14px; }

  .card--back .wordmark { left: 50%; top: 50%; transform: translate(-50%, -50%); }
  .card--back .wordmark__dot { width: 48px; height: 48px; margin-right: 20px; }
  .card--back .wordmark__main { font-size: 58px; }
  .card--back .wordmark__sub { font-size: 26px; }

  .divider {
    position: absolute;
    left: 322px;
    top: 106px;
    width: 2px;
    height: 180px;
    background: var(--rule);
  }
  .contact {
    position: absolute;
    left: 347px;
    top: 118px;
  }
  .contact__name {
    font-family: "Montserrat", sans-serif;
    font-weight: 300;
    font-size: 22px;
    color: var(--text-light);
    line-height: 1.2;
  }
  .contact__role {
    font-family: "Montserrat", sans-serif;
    font-weight: 300;
    font-size: 13px;
    color: var(--red);
    margin-top: 2px;
  }
  .contact__list { list-style: none; margin-top: 26px; }
  .contact__item {
    display: flex;
    align-items: center;
    font-size: 14px;
    color: var(--text-light);
    height: 28px;
    white-space: nowrap;
  }
  .contact__icon { width: 14px; height: 14px; margin-right: 10px; flex: none; }
</style>
</head>
<body>
  <section class="card card--front">
    <div class="wordmark">
      <span class="wordmark__dot"></span>
      <span class="wordmark__name">
        <span class="wordmark__main">BIRCHMEAD</span>
        <span class="wordmark__sub">Assurance Group Ltd</span>
      </span>
    </div>
    <div class="divider"></div>
    <div class="contact">
      <p class="contact__name">Clara Hotham</p>
      <p class="contact__role">Director</p>
      <ul class="contact__list">
        <li class="contact__item">
          <svg class="contact__icon" viewBox="0 0 14 14"><rect x="1" y="3" width="12" height="8" fill="var(--red)"/><path d="M1 3 L7 8 L13 3" stroke="#0c0c0c" stroke-width="1" fill="none"/></svg>
          chotham@bag-example.co.nz
        </li>
        <li class="contact__item">
          <svg class="contact__icon" viewBox="0 0 14 14"><rect x="3.5" y="1" width="7" height="12" rx="1" fill="none" stroke="var(--red)" stroke-width="1.3"/><circle cx="7" cy="11" r="0.8" fill="var(--red)"/></svg>
          +6427390516
        </li>
        <li class="contact__item">
          <svg class="contact__icon" viewBox="0 0 14 14"><path d="M7 13 C4 9 2.5 7 2.5 5 A4.5 4.5 0 0 1 11.5 5 C11.5 7 10 9 7 13 Z" fill="var(--red)"/><circle cx="7" cy="5" r="1.6" fill="#0c0c0c"/></svg>
          PO Box 419, Kowhai Ridge, KR,
        </li>
      </ul>
    </div>
  </section>

  <section class="card card--back">
    <div class="wordmark">
      <span class="wordmark__dot"></span>
      <span class="wordmark__name">
        <span class="wordmark__main">BIRCHMEAD</span>
        <span class="wordmark__sub">Assurance Group Ltd</span>
      </span>
    </div>
  </section>
</body>
</html>
```